Criação de Papelaria Profissional para Crianças & Infantil
A empresa queria:
" Esta empresa preza por vender roupas de altíssima qualidade e marcas diferenciadas, a fim de encantar pais e filhos, garantindo conforto e estilo aos pequenos. "

```html
<!DOCTYPE html>
<html lang="pt-BR">
<head>
<meta charset="utf-8">
<title>Lumibê – Assinatura de e-mail</title>
<link rel="stylesheet" href="https://fonts.googleapis.com/css2?family=Baloo+2:wght@600&family=Poppins:wght@500;600&display=swap">
<style>
  :root {
    --bg-purple: #6a2c7e;
    --panel-purple: #6d2a80;
    --card-white: #ffffff;
    --card-edge: #c9a9da;
    --brand-purple: #8c5bb7;
    --tagline-purple: #9a6cc0;
    --text-white: #ffffff;
    --icon-lilac: #d9b8ef;
    --stripe-blue: #7ec3e6;
    --stripe-yellow: #f4c15a;
    --stripe-pink: #ee8fa8;
    --stripe-sky: #9fd4f0;
  }
  * { box-sizing: border-box; margin: 0; padding: 0; }
  html, body { width: 1200px; height: 1200px; overflow: hidden; }
  body { background: var(--bg-purple); position: relative; font-family: "Poppins", sans-serif; }

  .signature-card {
    position: absolute; left: 60px; top: 451px; width: 1080px; height: 294px;
    border-radius: 34px; overflow: hidden; background: var(--card-white);
    border: 3px solid var(--card-edge);
    box-shadow: 0 18px 40px rgba(40, 8, 55, 0.45);
  }
  .card-shapes { position: absolute; inset: 0; }

  .brand-lockup { position: absolute; left: 90px; top: 74px; }
  .brand-name {
    display: flex; align-items: center; gap: 14px;
    font-family: "Baloo 2", sans-serif; font-weight: 600; font-size: 92px;
    line-height: 1; color: var(--brand-purple);
  }
  .brand-dot { width: 26px; height: 26px; border-radius: 50%; background: var(--brand-purple); }
  .brand-tagline {
    margin-top: 2px; margin-left: 132px; font-size: 17px; font-weight: 500;
    color: var(--tagline-purple); white-space: nowrap;
  }

  .contact-list { position: absolute; left: 590px; top: 42px; list-style: none; }
  .contact-item {
    display: flex; align-items: flex-start; gap: 12px;
    color: var(--text-white); font-size: 19px; font-weight: 600; line-height: 1.1;
    margin-bottom: 14px;
  }
  .contact-item svg { width: 20px; height: 20px; flex: none; margin-top: 1px; }
  .contact-address { margin-bottom: 0; }
</style>
</head>
<body>
  <section class="signature-card" aria-label="Assinatura de e-mail Lumibê">
    <svg class="card-shapes" viewBox="0 0 1074 288" preserveAspectRatio="none" aria-hidden="true">
      <path d="M562 0 H1074 V288 H562 C578 215 578 72 562 0 Z" fill="var(--panel-purple)"/>
      <rect x="0" y="277" width="150" height="11" fill="var(--stripe-blue)"/>
      <rect x="150" y="277" width="140" height="11" fill="var(--stripe-yellow)"/>
      <rect x="290" y="277" width="140" height="11" fill="var(--stripe-pink)"/>
      <rect x="430" y="277" width="135" height="11" fill="var(--stripe-sky)"/>
    </svg>

    <div class="brand-lockup">
      <div class="brand-name"><span class="brand-dot"></span>Lumibê</div>
      <p class="brand-tagline">Leveza para cada aventura</p>
    </div>

    <ul class="contact-list">
      <li class="contact-item">
        <svg viewBox="0 0 24 24" fill="none" stroke="var(--icon-lilac)" stroke-width="2"><circle cx="12" cy="12" r="9"/><path d="M9 8.5c0 3.5 3 6.5 6.5 6.5l1-1.5-2-1-1 1c-1-.5-2-1.5-2.5-2.5l1-1-1-2z" fill="var(--icon-lilac)" stroke="none"/></svg>
        <span>(00) 99999-0000</span>
      </li>
      <li class="contact-item">
        <svg viewBox="0 0 24 24" fill="none" stroke="var(--icon-lilac)" stroke-width="2" stroke-linejoin="round"><path d="M5 4h4l2 5-2.5 1.5a11 11 0 0 0 5 5L15 13l5 2v4a2 2 0 0 1-2 2A16 16 0 0 1 3 6a2 2 0 0 1 2-2z"/></svg>
        <span>(00) 3333-0000</span>
      </li>
      <li class="contact-item">
        <svg viewBox="0 0 24 24" fill="none" stroke="var(--icon-lilac)" stroke-width="2"><rect x="4" y="4" width="16" height="16" rx="5"/><circle cx="12" cy="12" r="3.5"/></svg>
        <span>@lumibe</span>
      </li>
      <li class="contact-item">
        <svg viewBox="0 0 24 24" fill="none" stroke="var(--icon-lilac)" stroke-width="2" stroke-linejoin="round"><rect x="3" y="5" width="18" height="14" rx="2"/><path d="M3 6l9 7 9-7"/></svg>
        <span>lumibe@exemplo.com</span>
      </li>
      <li class="contact-item contact-address">
        <svg viewBox="0 0 24 24" fill="none" stroke="var(--icon-lilac)" stroke-width="2"><path d="M12 22s7-7 7-12a7 7 0 0 0-14 0c0 5 7 12 7 12z"/><circle cx="12" cy="10" r="2.5"/></svg>
        <span>Endereço completo, 000<br>Bairro, CEP 00000-000<br>Cidade UF</span>
      </li>
    </ul>
  </section>
</body>
</html>
```